Business Card Design

Attached is the logo of the store.

Information needed on the business card:

www.brookvale17vino.com
info@brookvale17vino.com
412 Harlow St NY, NY 10027
Tel:(646) 472-3958

Store Hours
Mon-Sat 11am-9pm
Sun 1pm-7pm

Local Delivery

Industry/Entity Type

Business

Contact Information for Business Card

Brookvale 17 Wine & Spirits

```html
<!DOCTYPE html>
<html lang="en">
<head>
<meta charset="utf-8">
<title>Brookvale 17 Wine &amp; Spirits — Business Card</title>
<link href="https://fonts.googleapis.com/css2?family=Mulish:wght@700&display=swap" rel="stylesheet">
<style>
  :root {
    --backdrop: #262626;
    --card-front: #1f1f1f;
    --card-back: #9a8f8f;
    --ink-dark: #262424;
    --ink-light: #f2f2f2;
    --bottle-top: #1a1a1a;
    --bottle-bottom: #0c0c0c;
  }
  * { margin: 0; padding: 0; box-sizing: border-box; }
  html, body {
    width: 1200px;
    height: 900px;
    overflow: hidden;
    background: var(--backdrop);
  }
  .canvas {
    position: relative;
    width: 1200px;
    height: 900px;
    font-family: "Mulish", "Helvetica Neue", Arial, sans-serif;
  }
  .card {
    position: absolute;
    top: 326px;
    width: 427px;
    height: 250px;
    box-shadow: 0 4px 10px rgba(0,0,0,0.45);
  }
  .card--front {
    left: 65px;
    background: var(--card-front);
    display: flex;
    align-items: center;
    justify-content: center;
  }
  .brand-name {
    color: var(--ink-light);
    font-size: 22px;
    font-weight: 700;
    letter-spacing: 0.02em;
  }
  .card--back {
    left: 606px;
    background: var(--card-back);
    overflow: hidden;
  }
  .contact {
    position: absolute;
    left: 10px;
    top: 5px;
    list-style: none;
    color: var(--ink-dark);
    font-size: 13px;
    font-weight: 700;
    letter-spacing: 0.02em;
    line-height: 24px;
    white-space: nowrap;
  }
  .contact .gap { height: 24px; }
  .bottle-area {
    position: absolute;
    left: 250px;
    top: 0;
    width: 92px;
    height: 250px;
    background: linear-gradient(180deg, var(--bottle-top), var(--bottle-bottom));
  }
</style>
</head>
<body>
<main class="canvas">
  <section class="card card--front" aria-label="Card front">
    <h1 class="brand-name">Brookvale 17 Wine &amp; Spirits</h1>
  </section>

  <section class="card card--back" aria-label="Card back">
    <ul class="contact">
      <li>www.brookvale17vino.com</li>
      <li>info@brookvale17vino.com</li>
      <li>412 Harlow St NY, NY 10027</li>
      <li>Tel:(646) 472-3958</li>
      <li class="gap" aria-hidden="true"></li>
      <li>Store Hours</li>
      <li>Mon-Sat 11am-9pm</li>
      <li>Sun 1pm-7pm</li>
      <li class="gap" aria-hidden="true"></li>
      <li>Local Delivery</li>
    </ul>
    <div class="bottle-area" role="img" aria-label="Dark wine bottle with the store label"></div>
  </section>
</main>
</body>
</html>
```